Pocketly - New Payment App for Student

Pocket-ly - A Payment App for student to make payment, track own expenses and practice good dietary habits. The App theme is Fun and excitement.
Target User: Secondary Student aged 13-18
Look and Feel: Fun, excitement and simple.
Screen 1
Login to the app using thumbprints or password
Screen 2
Display the balance
Wallet balance >>> go to screen 3 to display transaction history
Gamification balance - points + badges >>> go to screen 3
Button to make payment
Screen 2-1
Allow them to do payment
Click “Pay”
Display QR code
scanning by merchant
Payment made
Notification received
The transaction history will be shown up
Screen 2-2
Allow them to top up (alternatively to parent Top-up using credit card)
Click “Top Up”
Display QR code
Pass the cash to merchant
scanning by merchant
Payment made
Notification received
The new balance will be shown up
Screen 3
Display more details on transaction history
Payment history + gamification history (gain/redeem points)
E.g. 14 Nov Canteen purchase $5.40
- Banana +30 points
- Milk +10 points
Screen 4 (play a game to earn point)
Introduce some trivial games (while waiting in line at cafeteria or school store) to gain some points
Crosswords
Puzzle
Screen 5 (Display achievements)
Leaderboard
Where the individual stands in the class
Where the class stands overall in school
Badges
Level
Achievements
For more, please go to our website http://www.pocketly.example/
Target Market(s)
Secondary School Student aged 13-18
Industry/Entity Type
Education
Logo Text
pocketly
Look and feel

```html
<!DOCTYPE html>
<html lang="en">
<head>
<meta charset="utf-8">
<title>Pocketly – Transactions</title>
<link href="https://fonts.googleapis.com/css2?family=Lato:wght@300;400;700;900&display=swap" rel="stylesheet">
<style>
  :root {
    --orange-top: #ff5400;
    --orange-bottom: #ff8a00;
    --accent: #ff6a13;
    --points: #ff9a1f;
    --amount: #ff7a3c;
    --indigo: #3a26b0;
    --violet: #c46ad8;
    --gold-top: #ffdc00;
    --gold-bottom: #ffb300;
    --button-text: #5a3b00;
    --ink: #111111;
    --muted: #7a7a7a;
    --tab-bg: #eeeeee;
    --divider: #e4e4e4;
    --white: #ffffff;
  }
  * { margin: 0; padding: 0; box-sizing: border-box; }
  html, body { width: 675px; height: 1200px; overflow: hidden; background: var(--white); }
  body { font-family: "Lato", Arial, sans-serif; position: relative; }

  .app-header {
    position: absolute; left: 0; top: 0; width: 675px; height: 113px;
    background: linear-gradient(180deg, var(--orange-top), var(--orange-bottom));
    color: var(--white);
  }
  .status-bar { position: absolute; left: 0; top: 0; width: 100%; height: 40px; font-size: 18px; }
  .status-bar .carrier { position: absolute; left: 10px; top: 9px; display: flex; align-items: center; gap: 6px; }
  .status-bar .time { position: absolute; left: 0; right: 0; top: 9px; text-align: center; }
  .status-bar .battery { position: absolute; right: 10px; top: 9px; display: flex; align-items: center; gap: 6px; }
  .page-title {
    position: absolute; left: 0; right: 0; top: 57px; text-align: center;
    font-size: 28px; font-weight: 700;
  }

  .balance-card {
    position: absolute; left: 0; top: 113px; width: 675px; height: 162px;
    background: linear-gradient(100deg, var(--indigo) 0%, #7a4cc4 50%, var(--violet) 100%);
    color: var(--white);
  }
  .balance-label { position: absolute; left: 36px; top: 44px; font-size: 22px; font-weight: 700; }
  .balance-value { position: absolute; left: 34px; top: 88px; font-size: 41px; font-weight: 300; }
  .top-up-button {
    position: absolute; left: 473px; top: 40px; width: 180px; height: 90px; border-radius: 45px;
    background: linear-gradient(180deg, var(--gold-top), var(--gold-bottom));
    color: var(--button-text); font-size: 22px; font-weight: 700;
    display: flex; align-items: center; justify-content: center;
  }

  .history-tabs { position: absolute; left: 0; top: 275px; width: 675px; height: 89px; }
  .history-title { position: absolute; left: 36px; top: 31px; font-size: 22px; font-weight: 700; color: var(--ink); }
  .month-picker {
    position: absolute; left: 337px; top: 0; width: 338px; height: 89px; background: var(--tab-bg);
    font-size: 22px; color: var(--muted);
  }
  .month-picker .month { position: absolute; left: 38px; top: 31px; }
  .month-picker .month b { font-weight: 700; }
  .month-picker .month span { font-weight: 400; }
  .month-picker svg { position: absolute; left: 283px; top: 37px; }

  .day-group {
    position: absolute; left: 0; width: 675px; height: 182px;
    border-bottom: 1.5px solid var(--divider);
  }
  .entry { position: absolute; left: 0; width: 675px; height: 30px; font-size: 23px; font-weight: 400; }
  .entry .day { position: absolute; left: 36px; color: var(--muted); }
  .entry .name { position: absolute; left: 109px; color: var(--ink); font-weight: 300; }
  .entry.summary .name { color: var(--muted); font-weight: 400; }
  .entry .points { position: absolute; right: 128px; color: var(--points); font-weight: 300; }
  .entry .amount { position: absolute; right: 22px; color: var(--amount); font-weight: 300; }
  .entry.summary .amount { font-weight: 900; color: var(--accent); }
  .row-1 { top: 31px; }
  .row-2 { top: 79px; }
  .row-3 { top: 121px; }

  .tab-bar { position: absolute; left: 0; top: 1091px; width: 675px; height: 109px; border-top: 1.5px solid var(--divider); background: var(--white); }
  .tab-icon { position: absolute; }
  .pay-button {
    position: absolute; left: 284px; top: 1094px; width: 108px; height: 108px; border-radius: 50%;
    background: var(--white); border: 11px solid var(--accent);
    display: flex; align-items: center; justify-content: center;
    color: var(--accent); font-size: 46px; font-weight: 900;
  }
</style>
</head>
<body>
  <header class="app-header">
    <div class="status-bar">
      <div class="carrier">
        <svg width="70" height="10" viewBox="0 0 70 10"><g fill="#fff"><circle cx="5" cy="5" r="4.5"/><circle cx="18" cy="5" r="4.5"/><circle cx="31" cy="5" r="4.5"/><circle cx="44" cy="5" r="4.5"/><circle cx="57" cy="5" r="4.5"/></g></svg>
        <span>Carrier</span>
        <svg width="20" height="15" viewBox="0 0 20 15"><path d="M10 14 L1 5 A13 13 0 0 1 19 5 Z" fill="#fff"/></svg>
      </div>
      <div class="time">9:41 AM</div>
      <div class="battery">
        <span>100%</span>
        <svg width="44" height="18" viewBox="0 0 44 18"><rect x="1" y="1" width="38" height="16" rx="3" fill="none" stroke="#fff" stroke-width="1.5"/><rect x="3.5" y="3.5" width="33" height="11" rx="1.5" fill="#fff"/><rect x="40.5" y="6" width="2.5" height="6" rx="1" fill="#fff"/></svg>
      </div>
    </div>
    <h1 class="page-title">Transactions</h1>
  </header>

  <section class="balance-card">
    <div class="balance-label">Current ballance</div>
    <div class="balance-value">$ 35.00</div>
    <div class="top-up-button">Top up</div>
  </section>

  <nav class="history-tabs">
    <div class="history-title">Transactions history</div>
    <div class="month-picker">
      <div class="month"><b>December</b> <span>2016</span></div>
      <svg width="20" height="12" viewBox="0 0 20 12"><polyline points="1,1 10,10 19,1" fill="none" stroke="#888" stroke-width="2"/></svg>
    </div>
  </nav>

  <section class="day-group" style="top:364px">
    <div class="entry summary row-1"><span class="day">20</span><span class="name">Daily ballance</span><span class="points">+50 points</span><span class="amount">($ 5.00)</span></div>
    <div class="entry row-2"><span class="name">Canteen food</span><span class="points">+50 points</span><span class="amount">($ 4.00)</span></div>
    <div class="entry row-3"><span class="name">Fizz-cola</span><span class="amount">($ 1.00)</span></div>
  </section>

  <section class="day-group" style="top:546px">
    <div class="entry summary row-1"><span class="day">19</span><span class="name">Daily ballance</span><span class="points">+50 points</span><span class="amount">($ 4.50)</span></div>
    <div class="entry row-2"><span class="name">Sandwich</span><span class="amount">($ 4.00)</span></div>
    <div class="entry row-3"><span class="name">Cold tea</span><span class="points">+50 points</span><span class="amount">($ 0.50)</span></div>
  </section>

  <section class="day-group" style="top:728px">
    <div class="entry summary row-1"><span class="day">18</span><span class="name">Daily ballance</span><span class="points">+100 points</span><span class="amount">($ 5.50)</span></div>
    <div class="entry row-2"><span class="name">Sandwich</span><span class="points">+50 points</span><span class="amount">($ 5.00)</span></div>
    <div class="entry row-3"><span class="name">Cold tea</span><span class="points">+50 points</span><span class="amount">($ 0.50)</span></div>
  </section>

  <section class="day-group" style="top:910px">
    <div class="entry summary row-1"><span class="day">17</span><span class="name">Daily ballance</span><span class="points">+50 points</span><span class="amount">($ 4.50)</span></div>
    <div class="entry row-2"><span class="name">Cheese burger</span><span class="amount">($ 4.00)</span></div>
    <div class="entry row-3"><span class="name">Cold tea</span><span class="points">+50 points</span><span class="amount">($ 0.50)</span></div>
  </section>

  <footer class="tab-bar">
    <svg class="tab-icon" style="left:61px;top:52px" width="40" height="38" viewBox="0 0 40 38"><path d="M3 18 L20 3 L37 18 M7 15 V36 H16 V24 H24 V36 H33 V15" fill="none" stroke="#111" stroke-width="2.2" stroke-linejoin="round"/></svg>
    <svg class="tab-icon" style="left:176px;top:52px" width="44" height="40" viewBox="0 0 44 40"><g fill="none" stroke="#ff6a13" stroke-width="2"><path d="M2 10 H30 M2 10 L9 3 M2 10 L9 17"/><path d="M14 30 H42 M42 30 L35 23 M42 30 L35 37"/></g></svg>
    <svg class="tab-icon" style="left:457px;top:54px" width="46" height="36" viewBox="0 0 46 36"><g fill="none" stroke="#111" stroke-width="2.2"><path d="M12 4 H34 C42 4 45 20 43 28 C41 34 35 33 31 26 H15 C11 33 5 34 3 28 C1 20 4 4 12 4 Z"/><path d="M10 15 H18 M14 11 V19"/><circle cx="31" cy="12" r="1.8"/><circle cx="35" cy="17" r="1.8"/></g></svg>
    <svg class="tab-icon" style="left:575px;top:50px" width="36" height="42" viewBox="0 0 36 42"><g fill="none" stroke="#111" stroke-width="2.2"><ellipse cx="18" cy="13" rx="9" ry="11"/><path d="M9 11 C13 5 23 5 27 11"/><path d="M2 41 V35 C2 29 8 27 12 26 L18 33 L24 26 C28 27 34 29 34 35 V41 Z"/></g></svg>
  </footer>
  <div class="pay-button">$</div>
</body>
</html>
```